Brindlemar Needs Several Greeting Card Shell Designs and Designs for 8.5" x 11" Prints

Brindlemar Ltd. Co. is a publisher of social expression in the form of acrostic poems on greeting cards, prints, mugs, T-shirts, and a host of other products. "Acrostic" simply means spelling out something going down the page. ALL of our products are done in the acrostic style.
We have the following needs:
1) Three feminine greeting card shells designs. One design should allow for up to six lines of text to be added later. The other two designs should allow for up to 10 lines of text to be added later. These designs will be mostly aimed at tweens to young adults.
2)Three masculine greeting card shells designs. One design should allow for up to six lines of text to be added later. The other two designs should allow for up to 10 lines of text to be added later. These designs will be mostly aimed at tweens to young adults.
3) Three feminine design shells for 8.5" x 11" prints, with room for text to be added later. These designs will be aimed at a more mature audience (young adults and up).
4) Three neutral design shells for 8.5" x 11" prints, with room for text to be added later. Three feminine design shells for 8.5" x 11" prints, with room for text to be added later. These designs will be aimed at a more mature audience (young adults and up).
For samples of previous designs, please go to http://www.brindlemar.biz. We are looking for more current, trendy designs.

```html
<!DOCTYPE html>
<html lang="en">
<head>
<meta charset="utf-8">
<title>Brindlemar Greeting Card Shells</title>
<link rel="stylesheet" href="https://fonts.googleapis.com/css2?family=Great+Vibes&family=Parisienne&family=EB+Garamond:wght@400;600&family=Crimson+Text&family=PT+Sans&display=swap">
<style>
  :root {
    --page: #ffffff;
    --label: #6f6f6f;
    --navy: #24295e;
    --ink: #1d1d2a;
    --halo: #ffffff;
    --rose-ink: #ffffff;
    --rose-glow: #a8324f;
    --blue-title: #2a3a9c;
  }
  * { box-sizing: border-box; margin: 0; padding: 0; }
  html, body { width: 702px; height: 1200px; overflow: hidden; background: var(--page); }
  .sheet { position: relative; width: 702px; height: 1200px; }

  .theme { position: absolute; left: 0; width: 702px; height: 290px; }
  .theme--one { top: 18px; }
  .theme--two { top: 320px; }
  .theme--three { top: 612px; }
  .theme--four { top: 906px; }

  .theme__label {
    position: absolute; left: 50px; top: 0;
    font: 400 17px/1 "PT Sans", sans-serif; color: var(--label);
  }

  .card { position: absolute; top: 24px; width: 180px; }
  .card:nth-of-type(1) { left: 21px; }
  .card:nth-of-type(2) { left: 264px; }
  .card:nth-of-type(3) { left: 500px; }

  .card__face {
    position: relative; width: 180px; height: 230px;
    border: 3px solid var(--navy); overflow: hidden;
  }
  .card__art { position: absolute; inset: 0; }
  .card__frame {
    position: absolute; inset: 8px 9px;
    border: 1px solid rgba(255,255,255,.7);
  }
  .card__title {
    position: absolute; left: 0; right: 0; top: 18px; text-align: center;
    font: 400 24px/1 "Great Vibes", cursive; color: var(--navy);
    text-shadow: 0 0 3px var(--halo), 0 0 6px var(--halo), 0 0 8px var(--halo);
  }
  .card__text {
    position: absolute; left: 6px; right: 6px; top: 52px; text-align: center;
    font: 600 10.6px/14px "EB Garamond", serif; color: var(--ink);
    text-shadow: 0 0 2px var(--halo), 0 0 3px var(--halo), 0 0 5px var(--halo), 0 0 6px var(--halo);
  }
  .card__text--six { top: 58px; font-size: 11.6px; line-height: 16px; }

  .card__caption {
    margin-top: 8px; text-align: center;
    font: 400 17px/1 "PT Sans", sans-serif; color: var(--label);
  }

  /* 1st theme: floral pinks, script body */
  .theme--one .card__title {
    top: 22px; font-family: "Parisienne", cursive; font-size: 25px; color: var(--rose-ink);
    text-shadow: 0 0 4px var(--rose-glow), 0 0 8px var(--rose-glow);
  }
  .theme--one .card__text {
    font: 400 11px/13.6px "Parisienne", cursive; color: var(--rose-ink);
    text-shadow: 0 0 3px var(--rose-glow), 0 0 5px var(--rose-glow);
  }
  .theme--one .card__text--six { top: 66px; font-size: 14px; line-height: 19px; }
  .card--blossom .card__face { border: 3px solid #1a0a0e; box-shadow: inset 0 0 0 3px #e8a3b4; }
  .card--blossom .card__art { background: radial-gradient(circle at 50% 40%, #f2b6c4, #d9768f 55%, #8c3346); }
  .card--rose .card__face { border: 3px solid #1a0a0e; }
  .card--rose .card__art { background: radial-gradient(circle at 50% 35%, #f4bccb, #d67e95 45%, #5b4a7e 85%, #2f8f5a); }
  .card--petals .card__face { border: 3px solid #8e1c35; }
  .card--petals .card__art { background: linear-gradient(160deg, #f6d2d8, #e2a3ae 50%, #c8727f); }

  /* 2nd theme: blues and teals */
  .card--tiles .card__face { border: 3px solid #1a2a80; }
  .card--tiles .card__art { background: linear-gradient(180deg, #6f9ea0, #3d6f75 60%, #2c4f55); }
  .card--tiles .card__frame { inset: 12px 14px; background: rgba(210,235,235,.55); border-color: rgba(255,255,255,.8); }
  .card--tiles .card__title {
    top: 24px; font: 400 22px/1 "Crimson Text", serif; color: var(--blue-title);
  }
  .card--tiles .card__text--six {
    top: 62px; font: 400 13.4px/19px "Crimson Text", serif; color: #2f3d4a; text-shadow: none;
  }
  .card--swirl .card__art { background: radial-gradient(circle at 50% 45%, #7fd4f4, #2aa3de 55%, #1b6fb5); }
  .card--swirl .card__frame { background: rgba(255,255,255,.12); }
  .card--shadow .card__art { background: radial-gradient(circle at 50% 40%, #5f9c94, #2d6a68 50%, #163c42); }

  /* 3rd theme: playful illustrations */
  .card--forest .card__face { border-color: #1f6e35; }
  .card--forest .card__art { background: linear-gradient(180deg, #d5ecc0, #9fd08a 45%, #e8d4a8 75%, #c9a98d); }
  .card--forest .card__title { color: #d8283c; }
  .card--stars .card__art { background: radial-gradient(circle at 50% 45%, #bfe8f8, #55b5e3 60%, #2a86c6); }
  .card--whale .card__art { background: linear-gradient(90deg, #f9e8a8, #fdf4d8 25%, #f5d7a3 50%, #d9ecd6 75%, #f4d1b5); }

  /* 4th theme: warm sunsets and checks */
  .card--dusk .card__art { background: linear-gradient(180deg, #d77fd3, #c86fc4 45%, #f0b36a 80%, #f5c46d); }
  .card--dusk .card__frame { border-color: rgba(240,210,120,.8); }
  .card--checks .card__face { border-color: #141414; }
  .card--checks .card__art { background: linear-gradient(180deg, #d59a45, #f5dcae 30%, #f3d2a0 70%, #b57a2e); }
  .card--checks .card__frame { inset: 14px 20px; background: rgba(255,240,215,.55); }
  .card--glow .card__face { border-color: #b3203b; }
  .card--glow .card__art { background: radial-gradient(circle at 50% 40%, #fde0b4, #f3a577 50%, #e06a6d); }
</style>
</head>
<body>
<main class="sheet">

  <section class="theme theme--one">
    <h2 class="theme__label">1st theme</h2>
    <figure class="card card--blossom">
      <div class="card__face">
        <div class="card__art" role="img" aria-label="Close-up photograph of pink cherry blossoms"></div>
        <div class="card__frame"></div>
        <h3 class="card__title">Lorem</h3>
        <p class="card__text card__text--six">Dolor sit amet,<br>consectetur adipisicing<br>elit, sed do eiusmod<br>tempor incididunt ut<br>labore et dolore magna<br>aliqua. Utt enim ad</p>
      </div>
      <figcaption class="card__caption">6 lines</figcaption>
    </figure>
    <figure class="card card--rose">
      <div class="card__face">
        <div class="card__art" role="img" aria-label="Soft-focus photograph of a pink rose"></div>
        <div class="card__frame"></div>
        <h3 class="card__title">Lorem</h3>
        <p class="card__text">Dolor sit amet, consectetur<br>adipisicing elit, sed do eiusmod<br>tempor incididunt ut labore et<br>dolore magna aliqua. Utt enim ad<br>minim veniam, quis nostrud<br>exercitation ullamco laboris<br>nisi ut aliquip ex ea commodo<br>consequat. Duis aute irure<br>dolor in reprehenderit in<br>voluptate velit esse cillum</p>
      </div>
      <figcaption class="card__caption">10 lines</figcaption>
    </figure>
    <figure class="card card--petals">
      <div class="card__face">
        <div class="card__art" role="img" aria-label="Pattern of pink and dark red flowers"></div>
        <div class="card__frame"></div>
        <h3 class="card__title">Lorem</h3>
        <p class="card__text">Dolor sit amet, consectetur<br>adipisicing elit, sed do eiusmod<br>tempor incididunt ut labore et<br>dolore magna aliqua. Utt enim ad<br>minim veniam, quis nostrud<br>exercitation ullamco laboris<br>nisi ut aliquip ex ea commodo<br>consequat. Duis aute irure<br>dolor in reprehenderit in<br>voluptate velit esse cillum</p>
      </div>
      <figcaption class="card__caption">10 lines</figcaption>
    </figure>
  </section>

  <section class="theme theme--two">
    <h2 class="theme__label">2nd theme</h2>
    <figure class="card card--tiles">
      <div class="card__face">
        <div class="card__art" role="img" aria-label="Teal graphic pattern of geometric shapes"></div>
        <div class="card__frame"></div>
        <h3 class="card__title">Lorem</h3>
        <p class="card__text card__text--six">Dolor sit amet,<br>consectetur<br>adipisicing elit, sed<br>do eiusmod tempor<br>incididunt ut labore<br>et dolore magna</p>
      </div>
      <figcaption class="card__caption">6 lines</figcaption>
    </figure>
    <figure class="card card--swirl">
      <div class="card__face">
        <div class="card__art" role="img" aria-label="Bright blue background with swirling graphic shapes"></div>
        <div class="card__frame"></div>
        <h3 class="card__title">Lorem</h3>
        <p class="card__text">Dolor sit amet, consectetur<br>adipisicing elit, sed do<br>eiusmod tempor incididunt<br>ut labore et dolore magna<br>aliqua. Utt enim ad minim<br>veniam, quis nostrud<br>exercitation ullamco laboris<br>nisi ut aliquip ex ea<br>commodo consequat. Duis<br>aute irure dolor in</p>
      </div>
      <figcaption class="card__caption">10 lines</figcaption>
    </figure>
    <figure class="card card--shadow">
      <div class="card__face">
        <div class="card__art" role="img" aria-label="Dark teal illustration of a hooded figure"></div>
        <div class="card__frame"></div>
        <h3 class="card__title">Lorem</h3>
        <p class="card__text">Dolor sit amet, consectetur<br>adipisicing elit, sed do<br>eiusmod tempor incididunt<br>ut labore et dolore magna<br>aliqua. Utt enim ad minim<br>veniam, quis nostrud<br>exercitation ullamco laboris<br>nisi ut aliquip ex ea<br>commodo consequat. Duis<br>aute irure dolor in</p>
      </div>
      <figcaption class="card__caption">10 lines</figcaption>
    </figure>
  </section>

  <section class="theme theme--three">
    <h2 class="theme__label">3rd theme</h2>
    <figure class="card card--forest">
      <div class="card__face">
        <div class="card__art" role="img" aria-label="Watercolour illustration of two children beside a large tree"></div>
        <div class="card__frame"></div>
        <h3 class="card__title">Lorem</h3>
        <p class="card__text card__text--six">Dolor sit amet,<br>consectetur adipisicing<br>elit, sed do eiusmod<br>tempor incididunt ut<br>labore et dolore magna<br>aliqua. Utt enim ad</p>
      </div>
      <figcaption class="card__caption">6 lines</figcaption>
    </figure>
    <figure class="card card--stars">
      <div class="card__face">
        <div class="card__art" role="img" aria-label="Blue illustration of floating toys and stars"></div>
        <div class="card__frame"></div>
        <h3 class="card__title">Lorem</h3>
        <p class="card__text">Dolor sit amet, consectetur<br>adipisicing elit, sed do<br>eiusmod tempor incididunt<br>ut labore et dolore magna<br>aliqua. Utt enim ad minim<br>veniam, quis nostrud<br>exercitation ullamco laboris<br>nisi ut aliquip ex ea<br>commodo consequat. Duis<br>aute irure dolor in</p>
      </div>
      <figcaption class="card__caption">10 lines</figcaption>
    </figure>
    <figure class="card card--whale">
      <div class="card__face">
        <div class="card__art" role="img" aria-label="Pastel illustration of a whale above striped buildings"></div>
        <div class="card__frame"></div>
        <h3 class="card__title">Lorem</h3>
        <p class="card__text">Dolor sit amet, consectetur<br>adipisicing elit, sed do<br>eiusmod tempor incididunt<br>ut labore et dolore magna<br>aliqua. Utt enim ad minim<br>veniam, quis nostrud<br>exercitation ullamco laboris<br>nisi ut aliquip ex ea<br>commodo consequat. Duis<br>aute irure dolor in</p>
      </div>
      <figcaption class="card__caption">10 lines</figcaption>
    </figure>
  </section>

  <section class="theme theme--four">
    <h2 class="theme__label">4th theme</h2>
    <figure class="card card--dusk">
      <div class="card__face">
        <div class="card__art" role="img" aria-label="Purple and orange sunset illustration with birds and a rooftop"></div>
        <div class="card__frame"></div>
        <h3 class="card__title">Lorem</h3>
        <p class="card__text card__text--six">Dolor sit amet, consectetur<br>adipisicing elit, sed do<br>eiusmod tempor incididunt<br>ut labore et dolore magna<br>aliqua. Utt enim ad minim<br>veniam, quis nostrud</p>
      </div>
      <figcaption class="card__caption">6 lines</figcaption>
    </figure>
    <figure class="card card--checks">
      <div class="card__face">
        <div class="card__art" role="img" aria-label="Black and cream checkerboard pattern with warm lighting"></div>
        <div class="card__frame"></div>
        <h3 class="card__title">Lorem</h3>
        <p class="card__text">Dolor sit amet, consectetur<br>adipisicing elit, sed do<br>eiusmod tempor incididunt<br>ut labore et dolore magna<br>aliqua. Utt enim ad minim<br>veniam, quis nostrud<br>exercitation ullamco laboris<br>nisi ut aliquip ex ea<br>commodo consequat. Duis<br>aute irure dolor in</p>
      </div>
      <figcaption class="card__caption">10 lines</figcaption>
    </figure>
    <figure class="card card--glow">
      <div class="card__face">
        <div class="card__art" role="img" aria-label="Warm peach and red illustration of glowing shapes"></div>
        <div class="card__frame"></div>
        <h3 class="card__title">Lorem</h3>
        <p class="card__text">Dolor sit amet, consectetur<br>adipisicing elit, sed do<br>eiusmod tempor incididunt<br>ut labore et dolore magna<br>aliqua. Utt enim ad minim<br>veniam, quis nostrud<br>exercitation ullamco laboris<br>nisi ut aliquip ex ea<br>commodo consequat. Duis<br>aute irure dolor in</p>
      </div>
      <figcaption class="card__caption">10 lines</figcaption>
    </figure>
  </section>

</main>
</body>
</html>
```